PowerPoint Master for IT company (Lumotrek GmbH)

As IT company we work in the fields Mobile, Big Data, Predictive Maintenance, Industry 4.0 and Data Science for the german Rail company "Nordwerk Schiene". We already have a Logo, coloring and a website (Attached Files).

What we need is a clear, professional and simple Design (nothing fancy) for PowerPoint/Word Master and Business Cards. Stockphotos from https://bildarchiv.nordwerkschiene.example/ can be used beside the attached logos.

We are a german company but would need either an universal or DE and EN template for PoerPoint.

Target Market(s)

IT, B2B, Rail companies, Industry

Contact Information for Business Card

- Logo
- Company Name
- Name
- Position
- Address
- Phone
- Mail

Font styles to use
Sans Serif

```html
<!DOCTYPE html>
<html lang="en">
<head>
<meta charset="utf-8">
<title>Lumotrek GmbH – Presentation Master</title>
<link href="https://fonts.googleapis.com/css2?family=Lato:wght@300;400;700;900&display=swap" rel="stylesheet">
<style>
:root{
  --navy:#1f2a63;
  --navy-dark:#141b45;
  --navy-mid:#34428a;
  --navy-soft:#5a68a8;
  --ice:#e9ecf5;
  --ink:#2b2f3a;
  --grey:#70757f;
  --line:#d6d9e3;
  --white:#ffffff;
  --photo-rail:linear-gradient(135deg,#8a9bb2 0%,#55657e 55%,#2e3a52 100%);
  --photo-land:linear-gradient(160deg,#b9c6d2 0%,#7f9570 50%,#4f6143 100%);
  --photo-truck:linear-gradient(150deg,#cfd6de 0%,#9aa5b2 55%,#5d6877 100%);
  --photo-night:linear-gradient(135deg,#3a4a72 0%,#1b2340 60%,#0e1328 100%);
  --photo-work:linear-gradient(150deg,#d9c27a 0%,#8a7c52 50%,#474a3c 100%);
}
*{box-sizing:border-box;margin:0;padding:0}
html,body{width:1200px;height:2949px;overflow:hidden;background:#fff}
body{font-family:"Lato",Arial,sans-serif;color:var(--ink)}
.icons-defs{position:absolute;width:0;height:0}
.deck{display:grid;grid-template-columns:repeat(3,392px);grid-template-rows:repeat(13,221px);column-gap:12px;row-gap:6px;width:1200px;height:2949px}
.slide{position:relative;overflow:hidden;background:#fff;box-shadow:0 0 0 1px #e3e5ec}
.abs{position:absolute}
.photo{position:absolute;background:var(--photo-rail)}
.photo.land{background:var(--photo-land)}
.photo.truck{background:var(--photo-truck)}
.photo.night{background:var(--photo-night)}
.photo.work{background:var(--photo-work)}
.s-title{position:absolute;left:14px;top:11px;font-size:13px;font-weight:900;color:var(--navy);text-transform:uppercase;letter-spacing:.2px}
.s-title.white{color:#fff}
.footer{position:absolute;left:0;right:0;bottom:0;height:15px;border-top:1px solid var(--line);background:#fff;display:flex;align-items:center;justify-content:space-between;padding:0 8px 0 12px;font-size:4.5px;color:var(--grey)}
.footer .f-brand{font-size:6px;font-weight:900;color:var(--navy);letter-spacing:.6px}
.footer .f-dot{width:10px;height:10px;border-radius:50%;border:1.5px solid var(--navy)}
.footer.dark{background:var(--navy);border-top:none;color:#c7cbe0}
.footer.dark .f-brand{color:#fff}
.footer.dark .f-dot{border-color:#fff}
.brand{display:flex;align-items:center;gap:5px;font-weight:900;letter-spacing:1px;color:#fff}
.brand .dot{width:12px;height:12px;border-radius:50%;border:2px solid currentColor}
.txt{font-size:5px;line-height:1.5;color:var(--grey)}
.txt.w{color:#d5d9ea}
.h{font-size:7px;font-weight:700;color:var(--navy);margin-bottom:2px}
.h.w{color:#fff}
.navy{background:var(--navy)}
.ico{width:14px;height:14px;fill:none;stroke:currentColor;stroke-width:1.6;stroke-linecap:round;stroke-linejoin:round}
.circle-ico{display:flex;align-items:center;justify-content:center;border-radius:50%}
.num{font-size:16px;font-weight:900;color:var(--line)}
table.data{border-collapse:collapse;width:100%;font-size:4.5px;color:var(--grey)}
table.data th{background:var(--navy);color:#fff;font-weight:700;height:10px}
table.data td{height:12px;border-bottom:1px solid var(--line);text-align:center}
table.data td:first-child{text-align:left;padding-left:6px}
table.data td.hl{background:var(--navy-mid);color:#fff}
table.data td.hl2{background:var(--navy);color:#fff}
.ring text{font-size:9px;font-weight:700;fill:#fff;font-family:"Lato",sans-serif}
.step-card{position:absolute;top:44px;width:104px;height:140px;border:1.5px solid var(--navy);border-radius:10px;padding:44px 8px 0}
.step-card .st{font-size:13px;font-weight:900;color:var(--navy)}
.icon-grid{position:absolute;left:22px;top:42px;display:grid;grid-template-columns:repeat(14,22px);gap:8px 2px;color:var(--navy)}
.icon-grid svg{width:14px;height:14px}
</style>
</head>
<body>
<svg class="icons-defs" aria-hidden="true">
  <defs>
    <symbol id="i-check" viewBox="0 0 16 16"><path d="M3 8.5l3 3 7-7"/></symbol>
    <symbol id="i-gear" viewBox="0 0 16 16"><circle cx="8" cy="8" r="2.5"/><path d="M8 1.5v2M8 12.5v2M1.5 8h2M12.5 8h2M3.4 3.4l1.4 1.4M11.2 11.2l1.4 1.4M3.4 12.6l1.4-1.4M11.2 4.8l1.4-1.4"/></symbol>
    <symbol id="i-chart" viewBox="0 0 16 16"><path d="M2 14h12M4 12V8M8 12V4M12 12V6"/></symbol>
    <symbol id="i-user" viewBox="0 0 16 16"><circle cx="8" cy="5.5" r="3"/><path d="M2.5 14.5c.8-3 3-4.5 5.5-4.5s4.7 1.5 5.5 4.5"/></symbol>
    <symbol id="i-pin" viewBox="0 0 16 16"><path d="M8 15s5-4.8 5-8.5a5 5 0 10-10 0C3 10.2 8 15 8 15z"/><circle cx="8" cy="6.5" r="1.8"/></symbol>
    <symbol id="i-phone" viewBox="0 0 16 16"><path d="M4 1.5h3l1 3.5-2 1.2a8 8 0 004 4l1.2-2 3.5 1v3c0 .8-.7 1.5-1.5 1.5C7 14 2 9 2.5 3 2.5 2.2 3.2 1.5 4 1.5z"/></symbol>
    <symbol id="i-mail" viewBox="0 0 16 16"><rect x="1.5" y="3.5" width="13" height="9" rx="1"/><path d="M1.5 4l6.5 5 6.5-5"/></symbol>
    <symbol id="i-globe" viewBox="0 0 16 16"><circle cx="8" cy="8" r="6.5"/><path d="M1.5 8h13M8 1.5c2 2 2.8 4.2 2.8 6.5S10 12.5 8 14.5C6 12.5 5.2 10.3 5.2 8S6 3.5 8 1.5z"/></symbol>
    <symbol id="i-doc" viewBox="0 0 16 16"><path d="M4 1.5h5.5L12.5 4.5v10h-8.5z"/><path d="M6 8h4.5M6 10.5h4.5"/></symbol>
    <symbol id="i-train" viewBox="0 0 16 16"><rect x="3.5" y="1.5" width="9" height="10" rx="2"/><path d="M3.5 7h9M5 14.5l1.5-3M11 14.5l-1.5-3"/></symbol>
  </defs>
</svg>

<main class="deck">

<!-- 1 title -->
<section class="slide">
  <div class="photo night" style="inset:0" role="img" aria-label="Dark station hall with a modern train at the platform"></div>
  <div class="abs" style="left:14px;top:16px"><div class="brand" style="font-size:9px"><span class="dot"></span>LUMOTREK</div></div>
  <div class="abs" style="left:14px;top:92px;color:#fff">
    <div style="font-size:20px;font-weight:900">PRESENTATION TITLE</div>
    <div style="font-size:7px;margin-top:3px;color:#cfd4ea">Your Subtitle Here</div>
  </div>
</section>

<!-- 2 title alt -->
<section class="slide">
  <div class="photo" style="left:0;top:0;right:0;height:130px" role="img" aria-label="Glass roof of a modern railway station"></div>
  <div class="abs navy" style="left:0;right:0;top:100px;bottom:0"></div>
  <div class="abs" style="right:16px;top:14px"><div class="brand" style="font-size:10px"><span class="dot"></span>LUMOTREK</div></div>
  <div class="abs" style="right:16px;top:132px;text-align:right;color:#fff">
    <div style="font-size:19px;font-weight:900">PRESENTATION TITLE</div>
    <div style="font-size:7px;color:#cfd4ea;margin-top:3px">Your Subtitle Here</div>
  </div>
  <div class="abs" style="right:16px;bottom:8px;font-size:5px;color:#b7bdd8">www.lumotrek.example</div>
</section>

<!-- 3 agenda -->
<section class="slide">
  <div class="photo" style="left:0;top:0;width:150px;bottom:15px" role="img" aria-label="High-speed train passing a green landscape"></div>
  <div class="s-title" style="left:170px">Agenda</div>
  <div class="abs" style="left:166px;top:34px;width:216px;display:grid;grid-template-columns:1fr 1fr;gap:10px 8px">
    <div><span class="num">01</span> <span class="h">Agenda One</span><div class="txt">Short note for this point.</div></div>
    <div><span class="num">04</span> <span class="h">Agenda One</span><div class="txt">Short note for this point.</div></div>
    <div><span class="num">02</span> <span class="h">Agenda One</span><div class="txt">Short note for this point.</div></div>
    <div><span class="num">05</span> <span class="h">Agenda One</span><div class="txt">Short note for this point.</div></div>
    <div><span class="num">03</span> <span class="h">Agenda One</span><div class="txt">Short note for this point.</div></div>
    <div><span class="num">06</span> <span class="h">Agenda One</span><div class="txt">Short note for this point.</div></div>
  </div>
  <div class="footer dark"><span class="f-brand">LUMOTREK</span><span>© Copyright 2019 Lumotrek GmbH. All rights reserved</span><span class="f-dot"></span></div>
</section>

<!-- 4 text slide -->
<section class="slide">
  <div class="s-title">Text Slide</div>
  <div class="abs txt" style="left:14px;right:14px;top:34px">
    <p>Our teams turn railway data into clear decisions. We combine mobile tools, big data platforms and predictive maintenance to keep fleets moving, reduce delays and plan repairs before faults appear. Every project starts with the questions of the people who run the network every day and ends with tools they enjoy using.</p>
    <p style="margin-top:6px">From sensors on the track to dashboards in the control room, we build the chain that links raw signals to useful insight. Industry 4.0 methods help us connect depots, workshops and operations into one shared picture, so that work orders, spare parts and staff can be planned with confidence and far less manual effort.</p>
    <p style="margin-top:6px">Data science gives the network a memory. We model wear, energy use and passenger flow, test our results with the experts in the field and deliver software that stays simple to run. This is how we help our partners grow with confidence today and in the years ahead.</p>
  </div>
  <div class="footer"><span class="f-brand">LUMOTREK</span><span>© Copyright 2019 Lumotrek GmbH. All rights reserved</span><span class="f-dot"></span></div>
</section>

<!-- 5 market overview -->
<section class="slide">
  <div class="s-title">Market Overview</div>
  <div class="abs navy" style="left:14px;top:34px;width:72px;height:100px;padding:8px;color:#fff">
    <svg class="ico" style="width:10px;height:10px"><use href="#i-chart"/></svg><div class="h w" style="font-size:5.5px">Heading Text</div>
    <svg class="ico" style="width:10px;height:10px;margin-top:8px"><use href="#i-gear"/></svg><div class="h w" style="font-size:5.5px">Heading Text</div><div class="txt w">Short note here.</div>
  </div>
  <div class="photo" style="left:92px;top:34px;width:66px;height:100px" role="img" aria-label="Modern office building facade"></div>
  <div class="abs navy" style="left:164px;top:34px;width:90px;height:100px;display:flex;align-items:center;justify-content:center">
    <svg width="56" height="56" viewBox="0 0 40 40" class="ring"><circle cx="20" cy="20" r="16" fill="none" stroke="#3b4a8f" stroke-width="4"/><circle cx="20" cy="20" r="16" fill="none" stroke="#fff" stroke-width="4" stroke-dasharray="60.3 100.5" transform="rotate(-90 20 20)"/><text x="20" y="23" text-anchor="middle">60%</text></svg>
  </div>
  <div class="abs" style="left:262px;top:34px;width:118px"><div class="h">Heading Text</div><div class="txt">Short note for this market segment.</div><div class="h" style="margin-top:8px">Heading Text</div><div class="txt">Short note for this market segment.</div></div>
  <div class="abs txt" style="left:92px;right:14px;top:142px">Demand for connected rail services keeps rising. Operators invest in sensors, data platforms and smart maintenance to raise availability and cut costs across their fleets and networks.</div>
  <div class="footer"><span class="f-brand">LUMOTREK</span><span>© Copyright 2019 Lumotrek GmbH. All rights reserved</span><span class="f-dot"></span></div>
</section>

<!-- 6 brand detailed -->
<section class="slide">
  <div class="s-title">Brand Detailed</div>
  <div class="photo land" style="left:14px;top:34px;width:210px;height:140px" role="img" aria-label="Passenger train on an autumn line"></div>
  <div class="abs" style="left:232px;top:34px;width:146px;display:grid;grid-template-columns:1fr 1fr;gap:4px">
    <div class="navy" style="height:68px;padding:6px"><div class="h w" style="font-size:5.5px">Vision</div><div class="txt w">Short note here.</div></div>
    <div class="navy" style="height:68px;padding:6px"><div class="h w" style="font-size:5.5px">Technology</div><div class="txt w">Short note here.</div></div>
    <div class="navy" style="height:68px;padding:6px"><div class="h w" style="font-size:5.5px">Mission</div><div class="txt w">Short note here.</div></div>
    <div class="navy" style="height:68px;padding:6px"><div class="h w" style="font-size:5.5px">Digital</div><div class="txt w">Short note here.</div></div>
  </div>
  <div class="footer"><span class="f-brand">LUMOTREK</span><span>© Copyright 2019 Lumotrek GmbH. All rights reserved</span><span class="f-dot"></span></div>
</section>

<!-- 7 vision & mission -->
<section class="slide">
  <div class="s-title">Our Vision &amp; Mission</div>
  <div class="photo night" style="left:14px;right:14px;top:32px;height:150px" role="img" aria-label="Night view of a city skyline in deep blue tones"></div>
  <div class="abs" style="left:26px;top:44px;width:160px;color:#fff">
    <div style="font-size:9px;font-weight:700">Our Vision:</div>
    <div style="font-size:9px;font-weight:700;line-height:1.2;margin:4px 0">Go to the Next Level Without look in the past</div>
    <div class="txt w">We make rail networks smarter with clear data and simple tools.</div>
  </div>
  <div class="abs" style="left:206px;top:44px;width:170px;color:#fff">
    <div style="font-size:9px;font-weight:700;margin-bottom:6px">Our Missions:</div>
    <div class="h w">Your Text Here</div><div class="txt w" style="margin-bottom:4px">Short note for this mission.</div>
    <div class="h w">Your Text Here</div><div class="txt w" style="margin-bottom:4px">Short note for this mission.</div>
    <div class="h w">Your Text Here</div><div class="txt w">Short note for this mission.</div>
  </div>
  <div class="footer"><span class="f-brand">LUMOTREK</span><span>© Copyright 2019 Lumotrek GmbH. All rights reserved</span><span class="f-dot"></span></div>
</section>

<!-- 8 four columns -->
<section class="slide">
  <div class="s-title">Your Title Here</div>
  <div class="abs" style="left:14px;right:14px;top:34px;height:148px;display:grid;grid-template-columns:repeat(4,1fr)">
    <div style="background:var(--navy);padding:10px 8px;color:#fff;text-align:center"><svg class="ico"><use href="#i-globe"/></svg><div class="h w" style="margin-top:8px">Heading Here</div><div class="txt w" style="text-align:left">Short text about this topic and what it brings to the project team.</div></div>
    <div style="background:var(--navy-mid);padding:10px 8px;color:#fff;text-align:center"><svg class="ico"><use href="#i-gear"/></svg><div class="h w" style="margin-top:8px">Heading Here</div><div class="txt w" style="text-align:left">Short text about this topic and what it brings to the project team.</div></div>
    <div style="background:var(--navy-soft);padding:10px 8px;color:#fff;text-align:center"><svg class="ico"><use href="#i-chart"/></svg><div class="h w" style="margin-top:8px">Heading Here</div><div class="txt w" style="text-align:left">Short text about this topic and what it brings to the project team.</div></div>
    <div style="background:var(--navy-dark);padding:10px 8px;color:#fff;text-align:center"><svg class="ico"><use href="#i-doc"/></svg><div class="h w" style="margin-top:8px">Heading Here</div><div class="txt w" style="text-align:left">Short text about this topic and what it brings to the project team.</div></div>
  </div>
  <div class="footer"><span class="f-brand">LUMOTREK</span><span>© Copyright 2019 Lumotrek GmbH. All rights reserved</span><span class="f-dot"></span></div>
</section>

<!-- 9 differences -->
<section class="slide">
  <div class="s-title">Our Differences</div>
  <div class="abs navy" style="left:14px;right:14px;top:34px;height:148px"></div>
  <div class="abs" style="left:24px;top:44px;width:200px;color:#fff">
    <div style="display:flex;gap:6px;margin-bottom:9px"><svg class="ico" style="width:10px;height:10px;flex:none"><use href="#i-check"/></svg><span class="txt w">Clear data pipelines from track sensors to the control room.</span></div>
    <div style="display:flex;gap:6px;margin-bottom:9px"><svg class="ico" style="width:10px;height:10px;flex:none"><use href="#i-check"/></svg><span class="txt w">Predictive models built with the people who run the fleet.</span></div>
    <div style="display:flex;gap:6px;margin-bottom:9px"><svg class="ico" style="width:10px;height:10px;flex:none"><use href="#i-check"/></svg><span class="txt w">Mobile tools that work in depots, yards and on the line.</span></div>
    <div style="display:flex;gap:6px"><svg class="ico" style="width:10px;height:10px;flex:none"><use href="#i-check"/></svg><span class="txt w">Simple software that stays easy to run for years.</span></div>
  </div>
  <div class="photo truck" style="left:236px;top:110px;width:134px;height:64px" role="img" aria-label="Trucks on a motorway"></div>
  <div class="footer"><span class="f-brand">LUMOTREK</span><span>© Copyright 2019 Lumotrek GmbH. All rights reserved</span><span class="f-dot"></span></div>
</section>

<!-- 10 title goes here grid -->
<section class="slide">
  <div class="s-title">Your Title Goes Here</div>
  <div class="abs" style="left:14px;right:14px;top:34px;height:148px;display:grid;grid-template-columns:1fr 1fr 1fr;grid-template-rows:1fr 1fr;gap:4px">
    <div class="photo truck" style="position:relative" role="img" aria-label="Truck on a road"></div>
    <div class="navy" style="display:flex;align-items:center;justify-content:center;color:#fff;font-size:8px;font-weight:700">Heading Goes Here</div>
    <div class="photo work" style="position:relative" role="img" aria-label="Track maintenance machine at work"></div>
    <div class="navy" style="display:flex;align-items:center;justify-content:center;color:#fff;font-size:8px;font-weight:700">Heading Goes Here</div>
    <div class="photo" style="position:relative" role="img" aria-label="Railway bridge at dusk"></div>
    <div class="navy" style="display:flex;align-items:center;justify-content:center;color:#fff;font-size:8px;font-weight:700">Heading Goes Here</div>
  </div>
  <div class="footer"><span class="f-brand">LUMOTREK</span><span>© Copyright 2019 Lumotrek GmbH. All rights reserved</span><span class="f-dot"></span></div>
</section>

<!-- 11 bullets and image -->
<section class="slide">
  <div class="s-title">Bullets and Image</div>
  <div class="abs" style="left:14px;top:36px;width:180px">
    <div style="display:flex;gap:5px;margin-bottom:8px"><span style="width:5px;height:5px;background:var(--navy);flex:none;margin-top:2px"></span><span class="txt">Sensor data from each train is checked in real time and stored in one secure platform.</span></div>
    <div style="display:flex;gap:5px;margin-bottom:8px"><span style="width:5px;height:5px;background:var(--navy);flex:none;margin-top:2px"></span><span class="txt">Maintenance teams receive alerts before faults cause delays on the line.</span></div>
    <div style="display:flex;gap:5px;margin-bottom:8px"><span style="width:5px;height:5px;background:var(--navy);flex:none;margin-top:2px"></span><span class="txt">Planners see the full state of the fleet on one clear dashboard.</span></div>
    <div style="display:flex;gap:5px"><span style="width:5px;height:5px;background:var(--navy);flex:none;margin-top:2px"></span><span class="txt">Reports are shared with every depot in a single click.</span></div>
  </div>
  <div class="photo work" style="left:204px;right:14px;top:34px;height:148px" role="img" aria-label="Yellow track maintenance vehicle on rails"></div>
  <div class="footer"><span class="f-brand">LUMOTREK</span><span>© Copyright 2019 Lumotrek GmbH. All rights reserved</span><span class="f-dot"></span></div>
</section>

<!-- 12 quote -->
<section class="slide">
  <div class="s-title">Quote Slide</div>
  <div class="abs" style="left:14px;top:40px;font-size:56px;font-weight:900;color:var(--navy);line-height:1">“</div>
  <div class="abs" style="left:46px;top:60px;width:150px">
    <div style="font-size:6.5px;line-height:1.5;color:var(--ink)">Good data does not replace experience on the track, it gives that experience a clear voice across the whole network and helps every team act sooner.</div>
    <div class="txt" style="text-align:right;margin-top:6px">JOHN DOE</div>
  </div>
  <div class="photo truck" style="left:208px;right:0;top:0;bottom:15px" role="img" aria-label="White truck on a logistics yard"></div>
  <div class="abs" style="right:14px;bottom:24px;display:flex;gap:5px"><span style="width:9px;height:9px;border-radius:50%;background:var(--navy)"></span><span style="width:9px;height:9px;border-radius:50%;background:var(--navy-mid)"></span><span style="width:9px;height:9px;border-radius:50%;background:var(--navy-soft)"></span></div>
  <div class="footer"><span class="f-brand">LUMOTREK</span><span>© Copyright 2019 Lumotrek GmbH. All rights reserved</span><span class="f-dot"></span></div>
</section>

<!-- 13 text + image -->
<section class="slide">
  <div class="s-title">Text + Image</div>
  <div class="abs" style="left:14px;top:38px;width:110px">
    <div class="txt" style="margin-bottom:7px">■ Short point about this service and its value for rail operators.</div>
    <div class="txt" style="margin-bottom:7px">■ Short point about this service and its value for rail operators.</div>
    <div class="txt" style="margin-bottom:7px">■ Short point about this service and its value for rail operators.</div>
    <div class="txt">■ Short point about this service and its value for rail operators.</div>
  </div>
  <div class="photo truck" style="left:130px;top:34px;width:140px;height:148px" role="img" aria-label="Hand pressing a button on a vehicle dashboard"></div>
  <div class="abs" style="left:280px;top:40px;width:100px">
    <div class="h">Heading Here</div><div class="txt" style="margin-bottom:8px">Short note about this point.</div>
    <div class="h">Heading Here</div><div class="txt" style="margin-bottom:8px">Short note about this point.</div>
    <div class="h">Heading Here</div><div class="txt">Short note about this point.</div>
  </div>
  <div class="footer"><span class="f-brand">LUMOTREK</span><span>© Copyright 2019 Lumotrek GmbH. All rights reserved</span><span class="f-dot"></span></div>
</section>

<!-- 14 two column text -->
<section class="slide">
  <div class="s-title">Two Column Text</div>
  <div class="abs" style="left:14px;top:38px;width:110px">
    <div class="h">• Your Heading Here</div><div class="txt" style="margin-bottom:8px">Short note about this topic and its main benefit.</div>
    <div class="h">• Your Heading Here</div><div class="txt" style="margin-bottom:8px">Short note about this topic and its main benefit.</div>
    <div class="h">• Your Heading Here</div><div class="txt">Short note about this topic and its main benefit.</div>
  </div>
  <div class="photo" style="left:130px;top:34px;width:120px;height:148px" role="img" aria-label="Close-up of a car dashboard control"></div>
  <div class="abs navy" style="left:256px;right:14px;top:34px;height:148px;padding:10px 8px">
    <div class="h w">• Your Heading Here</div><div class="txt w" style="margin-bottom:10px">Short note about this topic and its main benefit.</div>
    <div class="h w">• Your Heading Here</div><div class="txt w">Short note about this topic and its main benefit.</div>
  </div>
  <div class="footer"><span class="f-brand">LUMOTREK</span><span>© Copyright 2019 Lumotrek GmbH. All rights reserved</span><span class="f-dot"></span></div>
</section>

<!-- 15 three column -->
<section class="slide">
  <div class="s-title">Three Column Text</div>
  <div class="abs" style="left:14px;top:38px;width:250px;display:grid;grid-template-columns:repeat(3,1fr);gap:8px">
    <div><div class="h">Heading Here</div><div class="txt">Short text about this column. It explains one idea in a few plain words for the reader and closes with a clear result.</div></div>
    <div><div class="h">Heading Here</div><div class="txt">Short text about this column. It explains one idea in a few plain words for the reader and closes with a clear result.</div></div>
    <div><div class="h">Heading Here</div><div class="txt">Short text about this column. It explains one idea in a few plain words for the reader and closes with a clear result.</div></div>
  </div>
  <div class="photo truck" style="left:274px;right:14px;top:34px;height:148px" role="img" aria-label="Front of a white truck"></div>
  <div class="footer"><span class="f-brand">LUMOTREK</span><span>© Copyright 2019 Lumotrek GmbH. All rights reserved</span><span class="f-dot"></span></div>
</section>

<!-- 16 services -->
<section class="slide">
  <div class="s-title">Our Services</div>
  <div class="abs" style="left:14px;right:14px;top:32px;height:152px;display:grid;grid-template-columns:1fr 1fr;gap:5px">
    <div style="display:flex"><div class="photo work" style="position:relative;width:70px" role="img" aria-label="Workers on a track site"></div><div class="navy" style="flex:1;padding:8px"><div class="h w">Service Name</div><div class="txt w">Short note about this service.</div></div></div>
    <div style="display:flex"><div class="photo truck" style="position:relative;width:70px" role="img" aria-label="Truck fleet in a row"></div><div class="navy" style="flex:1;padding:8px"><div class="h w">Service Name</div><div class="txt w">Short note about this service.</div></div></div>
    <div style="display:flex"><div class="photo land" style="position:relative;width:70px" role="img" aria-label="Crane at a rail freight yard"></div><div class="navy" style="flex:1;padding:8px"><div class="h w">Service Name</div><div class="txt w">Short note about this service.</div></div></div>
    <div style="display:flex"><div class="photo" style="position:relative;width:70px" role="img" aria-label="Train in a station"></div><div class="navy" style="flex:1;padding:8px"><div class="h w">Service Name</div><div class="txt w">Short note about this service.</div></div></div>
  </div>
  <div class="footer"><span class="f-brand">LUMOTREK</span><span>© Copyright 2019 Lumotrek GmbH. All rights reserved</span><span class="f-dot"></span></div>
</section>

<!-- 17 divider -->
<section class="slide" style="background:var(--navy)">
  <div class="photo night" style="left:180px;right:0;top:0;bottom:0;opacity:.55" role="img" aria-label="Hand holding a smartphone, faded in blue"></div>
  <div class="abs" style="left:20px;top:92px;display:flex;align-items:center;gap:10px;color:#fff">
    <span style="width:26px;height:26px;border-radius:50%;border:3px solid #fff"></span>
    <div><div style="font-size:15px;font-weight:900">THIS IS YOUR DIVIDER PAGE</div><div style="font-size:6px;color:#c7cbe0;margin-top:2px">YOUR SUBTITLE HERE</div></div>
  </div>
</section>

<!-- 18 table -->
<section class="slide">
  <div class="s-title">Your Table Slide</div>
  <div class="abs" style="left:14px;right:14px;top:34px">
    <table class="data">
      <tr><th>Lorem</th><th>Value</th><th>Value</th><th>Value</th><th>Value</th></tr>
      <tr><td>Row item</td><td>12</td><td>24</td><td class="hl">54%</td><td>26</td></tr>
      <tr><td>Row item</td><td>15</td><td>20</td><td class="hl2">61%</td><td>31</td></tr>
      <tr><td>Row item</td><td>18</td><td>32</td><td class="hl">48%</td><td>27</td></tr>
      <tr><td>Row item</td><td>21</td><td>28</td><td class="hl2">72%</td><td>35</td></tr>
      <tr><td>Row item</td><td>11</td><td>36</td><td class="hl">39%</td><td>22</td></tr>
      <tr><td>Row item</td><td>17</td><td>30</td><td class="hl2">66%</td><td>29</td></tr>
      <tr><td>Row item</td><td>14</td><td>25</td><td class="hl">57%</td><td>33</td></tr>
      <tr><td>Row item</td><td>19</td><td>27</td><td class="hl2">44%</td><td>24</td></tr>
    </table>
  </div>
  <div class="footer"><span class="f-brand">LUMOTREK</span><span>© Copyright 2019 Lumotrek GmbH. All rights reserved</span><span class="f-dot"></span></div>
</section>

<!-- 19 panel + list -->
<section class="slide">
  <div class="abs navy" style="left:0;top:0;width:120px;bottom:15px"></div>
  <div class="abs" style="left:14px;top:128px;width:96px;color:#fff">
    <svg class="ico" style="width:12px;height:12px"><use href="#i-user"/></svg>
    <div style="font-size:9px;font-weight:900;margin:4px 0">WRITE HERE FOR YOU.</div>
    <div class="txt w">Short note about this idea and its value for the team.</div>
  </div>
  <div class="abs" style="left:134px;top:22px;width:240px">
    <div class="h">■ Your Heading Here</div><div class="txt" style="margin:0 0 8px 8px">Short note about this point and the result it brings.</div>
    <div class="h">■ Your Heading Here</div><div class="txt" style="margin:0 0 8px 8px">Short note about this point and the result it brings.</div>
    <div class="h">■ Your Heading Here</div><div class="txt" style="margin:0 0 8px 8px">Short note about this point and the result it brings.</div>
    <div class="h">■ Your Heading Here</div><div class="txt" style="margin-left:8px">Short note about this point and the result it brings.</div>
  </div>
  <div class="footer"><span class="f-brand">LUMOTREK</span><span>© Copyright 2019 Lumotrek GmbH. All rights reserved</span><span class="f-dot"></span></div>
</section>

<!-- 20 team single -->
<section class="slide">
  <div class="s-title">Our Team</div>
  <div class="abs" style="left:146px;top:34px;width:100px;height:100px;border-radius:50%;background:linear-gradient(160deg,#c9ced8,#8d96a8)" role="img" aria-label="Portrait photo of a team member"></div>
  <div class="abs" style="left:0;right:0;top:140px;text-align:center">
    <div class="h" style="font-size:6px">Mr. Team Lead</div>
    <div class="txt">Short note about this team member.</div>
    <div style="display:flex;gap:4px;justify-content:center;margin-top:5px"><span style="width:7px;height:7px;border-radius:50%;background:var(--navy)"></span><span style="width:7px;height:7px;border-radius:50%;background:var(--navy)"></span><span style="width:7px;height:7px;border-radius:50%;background:var(--navy)"></span><span style="width:7px;height:7px;border-radius:50%;background:var(--navy)"></span></div>
  </div>
  <div class="footer"><span class="f-brand">LUMOTREK</span><span>© Copyright 2019 Lumotrek GmbH. All rights reserved</span><span class="f-dot"></span></div>
</section>

<!-- 21 team four -->
<section class="slide">
  <div class="s-title">Our Team</div>
  <div class="abs" style="left:14px;right:14px;top:36px;display:grid;grid-template-columns:1fr 1fr;gap:12px 10px">
    <div style="display:flex;gap:6px"><div style="width:30px;height:30px;border-radius:50%;flex:none;background:linear-gradient(160deg,#c9ced8,#8d96a8)" role="img" aria-label="Portrait photo"></div><div><div class="h">Michael Doe</div><div class="txt">Manager</div><div class="txt">Short note about this role in the team.</div></div></div>
    <div style="display:flex;gap:6px"><div style="width:30px;height:30px;border-radius:50%;flex:none;background:linear-gradient(160deg,#c9ced8,#8d96a8)" role="img" aria-label="Portrait photo"></div><div><div class="h">James Doe</div><div class="txt">Manager</div><div class="txt">Short note about this role in the team.</div></div></div>
    <div style="display:flex;gap:6px"><div style="width:30px;height:30px;border-radius:50%;flex:none;background:linear-gradient(160deg,#c9ced8,#8d96a8)" role="img" aria-label="Portrait photo"></div><div><div class="h">Lena Doe</div><div class="txt">Manager</div><div class="txt">Short note about this role in the team.</div></div></div>
    <div style="display:flex;gap:6px"><div style="width:30px;height:30px;border-radius:50%;flex:none;background:linear-gradient(160deg,#c9ced8,#8d96a8)" role="img" aria-label="Portrait photo"></div><div><div class="h">John Doe</div><div class="txt">Manager</div><div class="txt">Short note about this role in the team.</div></div></div>
  </div>
  <div class="footer"><span class="f-brand">LUMOTREK</span><span>© Copyright 2019 Lumotrek GmbH. All rights reserved</span><span class="f-dot"></span></div>
</section>

<!-- 22 divider 2 -->
<section class="slide" style="background:var(--navy-dark)">
  <div class="photo night" style="inset:0;opacity:.7" role="img" aria-label="Station concourse in dark blue tones"></div>
  <div class="abs" style="left:0;right:0;top:62px;text-align:center;color:#fff">
    <div class="brand" style="justify-content:center;font-size:13px"><span class="dot"></span>LUMOTREK</div>
    <div style="font-size:18px;font-weight:900;margin-top:14px">THIS IS YOUR DIVIDER PAGE</div>
    <div style="font-size:6px;color:#c7cbe0;margin-top:3px">YOUR SUBTITLE HERE</div>
  </div>
</section>

<!-- 23 mock up -->
<section class="slide">
  <div class="s-title">Our Mock Up</div>
  <div class="abs" style="left:14px;top:34px;width:180px;height:148px;background:linear-gradient(160deg,#eef0f5,#c7ccd8)" role="img" aria-label="Desktop monitor and smartphone showing the website"></div>
  <div class="abs" style="left:210px;top:44px;width:170px">
    <div style="display:flex;gap:6px;margin-bottom:12px;color:var(--navy)"><svg class="ico" style="width:12px;height:12px;flex:none"><use href="#i-doc"/></svg><div><div class="h">Heading Here</div><div class="txt">Short note about this feature.</div></div></div>
    <div style="display:flex;gap:6px;margin-bottom:12px;color:var(--navy)"><svg class="ico" style="width:12px;height:12px;flex:none"><use href="#i-globe"/></svg><div><div class="h">Heading Here</div><div class="txt">Short note about this feature.</div></div></div>
    <div style="display:flex;gap:6px;color:var(--navy)"><svg class="ico" style="width:12px;height:12px;flex:none"><use href="#i-chart"/></svg><div><div class="h">Heading Here</div><div class="txt">Short note about this feature.</div></div></div>
  </div>
  <div class="footer"><span class="f-brand">LUMOTREK</span><span>© Copyright 2019 Lumotrek GmbH. All rights reserved</span><span class="f-dot"></span></div>
</section>

<!-- 24 pie -->
<section class="slide">
  <div class="s-title">Bullet &amp; Chart Area</div>
  <div class="abs" style="left:36px;top:44px;width:130px;height:130px;border-radius:50%;background:conic-gradient(#3b4a8f 0 36deg,#7a86bd 36deg 90deg,#2a3773 90deg 180deg,#141b45 180deg 360deg)"></div>
  <div class="abs" style="left:92px;top:32px;font-size:8px;font-weight:700;color:var(--navy)">10%</div>
  <div class="abs" style="left:18px;top:80px;font-size:8px;font-weight:700;color:var(--navy)">15%</div>
  <div class="abs" style="left:14px;top:128px;font-size:8px;font-weight:700;color:var(--navy)">25%</div>
  <div class="abs" style="left:172px;top:104px;font-size:8px;font-weight:700;color:var(--navy)">60%</div>
  <div class="abs" style="left:240px;top:44px;width:140px">
    <div style="display:flex;gap:6px;margin-bottom:10px"><span style="width:10px;height:10px;background:#3b4a8f;flex:none"></span><div><div class="h">Category One</div><div class="txt">Short note here.</div></div></div>
    <div style="display:flex;gap:6px;margin-bottom:10px"><span style="width:10px;height:10px;background:#7a86bd;flex:none"></span><div><div class="h">Category Two</div><div class="txt">Short note here.</div></div></div>
    <div style="display:flex;gap:6px;margin-bottom:10px"><span style="width:10px;height:10px;background:#2a3773;flex:none"></span><div><div class="h">Category Three</div><div class="txt">Short note here.</div></div></div>
    <div style="display:flex;gap:6px"><span style="width:10px;height:10px;background:#141b45;flex:none"></span><div><div class="h">Category Four</div><div class="txt">Short note here.</div></div></div>
  </div>
  <div class="footer"><span class="f-brand">LUMOTREK</span><span>© Copyright 2019 Lumotrek GmbH. All rights reserved</span><span class="f-dot"></span></div>
</section>

<!-- 25 bars -->
<section class="slide">
  <div class="s-title">Bullet &amp; Chart Area</div>
  <div class="abs" style="left:14px;top:38px;width:150px">
    <div style="display:flex;gap:8px;margin-bottom:9px"><span style="font-size:13px;font-weight:700;color:var(--navy)">50%</span><div><div class="h">Your Text Here</div><div class="txt">Short note here.</div></div></div>
    <div style="display:flex;gap:8px;margin-bottom:9px"><span style="font-size:13px;font-weight:700;color:var(--navy)">50%</span><div><div class="h">Your Text Here</div><div class="txt">Short note here.</div></div></div>
    <div style="display:flex;gap:8px;margin-bottom:9px"><span style="font-size:13px;font-weight:700;color:var(--navy)">50%</span><div><div class="h">Your Text Here</div><div class="txt">Short note here.</div></div></div>
    <div style="display:flex;gap:8px"><span style="font-size:13px;font-weight:700;color:var(--navy)">50%</span><div><div class="h">Your Text Here</div><div class="txt">Short note here.</div></div></div>
  </div>
  <div class="abs" style="left:190px;right:16px;top:44px;height:124px;border-bottom:1px solid var(--line);display:flex;align-items:flex-end;justify-content:space-around">
    <div style="display:flex;gap:2px;align-items:flex-end"><span style="width:8px;height:60px;background:var(--navy)"></span><span style="width:8px;height:80px;background:var(--navy-mid)"></span><span style="width:8px;height:45px;background:var(--navy-soft)"></span></div>
    <div style="display:flex;gap:2px;align-items:flex-end"><span style="width:8px;height:96px;background:var(--navy)"></span><span style="width:8px;height:70px;background:var(--navy-mid)"></span><span style="width:8px;height:55px;background:var(--navy-soft)"></span></div>
    <div style="display:flex;gap:2px;align-items:flex-end"><span style="width:8px;height:50px;background:var(--navy)"></span><span style="width:8px;height:88px;background:var(--navy-mid)"></span><span style="width:8px;height:64px;background:var(--navy-soft)"></span></div>
    <div style="display:flex;gap:2px;align-items:flex-end"><span style="width:8px;height:76px;background:var(--navy)"></span><span style="width:8px;height:58px;background:var(--navy-mid)"></span><span style="width:8px;height:110px;background:var(--navy-soft)"></span></div>
  </div>
  <div class="footer"><span class="f-brand">LUMOTREK</span><span>© Copyright 2019 Lumotrek GmbH. All rights reserved</span><span class="f-dot"></span></div>
</section>

<!-- 26 image + icons -->
<section class="slide">
  <div class="s-title">Image + Icons</div>
  <div class="photo night" style="left:0;right:0;top:30px;height:84px" role="img" aria-label="Operator in front of a wall of monitors"></div>
  <div class="abs" style="left:14px;right:14px;top:96px;display:grid;grid-template-columns:repeat(4,1fr);gap:6px;text-align:center">
    <div><div class="circle-ico navy" style="width:36px;height:36px;margin:0 auto;color:#fff;border:2px solid #fff"><svg class="ico"><use href="#i-chart"/></svg></div><div class="h" style="margin-top:5px">Heading Goes Here</div><div class="txt">Short note about this point.</div></div>
    <div><div class="circle-ico navy" style="width:36px;height:36px;margin:0 auto;color:#fff;border:2px solid #fff"><svg class="ico"><use href="#i-gear"/></svg></div><div class="h" style="margin-top:5px">Heading Goes Here</div><div class="txt">Short note about this point.</div></div>
    <div><div class="circle-ico navy" style="width:36px;height:36px;margin:0 auto;color:#fff;border:2px solid #fff"><svg class="ico"><use href="#i-globe"/></svg></div><div class="h" style="margin-top:5px">Heading Goes Here</div><div class="txt">Short note about this point.</div></div>
    <div><div class="circle-ico navy" style="width:36px;height:36px;margin:0 auto;color:#fff;border:2px solid #fff"><svg class="ico"><use href="#i-doc"/></svg></div><div class="h" style="margin-top:5px">Heading Goes Here</div><div class="txt">Short note about this point.</div></div>
  </div>
  <div class="footer"><span class="f-brand">LUMOTREK</span><span>© Copyright 2019 Lumotrek GmbH. All rights reserved</span><span class="f-dot"></span></div>
</section>

<!-- 27 image + bullets + text -->
<section class="slide">
  <div class="s-title">Image + Bullets + Text</div>
  <div class="abs" style="left:14px;top:36px;width:160px">
    <div style="display:flex;gap:6px;margin-bottom:8px"><div class="circle-ico navy" style="width:16px;height:16px;color:#fff;flex:none"><svg class="ico" style="width:9px;height:9px"><use href="#i-check"/></svg></div><div><div class="h">Heading Goes Here</div><div class="txt">Short note about this point.</div></div></div>
    <div style="display:flex;gap:6px;margin-bottom:8px"><div class="circle-ico navy" style="width:16px;height:16px;color:#fff;flex:none"><svg class="ico" style="width:9px;height:9px"><use href="#i-check"/></svg></div><div><div class="h">Heading Goes Here</div><div class="txt">Short note about this point.</div></div></div>
    <div style="display:flex;gap:6px"><div class="circle-ico navy" style="width:16px;height:16px;color:#fff;flex:none"><svg class="ico" style="width:9px;height:9px"><use href="#i-check"/></svg></div><div><div class="h">Heading Goes Here</div><div class="txt">Short note about this point.</div></div></div>
  </div>
  <div class="photo night" style="left:190px;right:0;top:30px;bottom:15px" role="img" aria-label="Track works lit at night"></div>
  <div class="abs" style="left:14px;top:150px;width:200px;font-size:6.5px;color:var(--navy);line-height:1.4">Short summary sentence about this project and its results, placed below the list.</div>
  <div class="footer"><span class="f-brand">LUMOTREK</span><span>© Copyright 2019 Lumotrek GmbH. All rights reserved</span><span class="f-dot"></span></div>
</section>

<!-- 28 blank -->
<section class="slide">
  <div class="s-title">Your Blank Slide</div>
  <div class="footer"><span class="f-brand">LUMOTREK</span><span>© Copyright 2019 Lumotrek GmbH. All rights reserved</span><span class="f-dot"></span></div>
</section>

<!-- 29 images + text -->
<section class="slide">
  <div class="s-title">Images + Text</div>
  <div class="abs navy" style="left:14px;top:32px;width:240px;height:68px;padding:8px;color:#fff">
    <div style="font-size:10px;font-weight:900">HEADING HERE</div>
    <div class="txt w" style="margin-top:3px">Short text about this project. It explains the goal, the approach and the result in a few plain words.</div>
  </div>
  <div class="abs" style="left:260px;right:14px;top:32px;height:68px;background:var(--navy-mid);padding:8px" >
    <div class="txt w">Short note about this image and its role in the story.</div>
  </div>
  <div class="photo land" style="left:14px;top:106px;width:180px;height:76px" role="img" aria-label="Railway line through green fields"></div>
  <div class="photo truck" style="left:200px;right:14px;top:106px;height:76px" role="img" aria-label="Passenger car on a rail shuttle"></div>
  <div class="footer"><span class="f-brand">LUMOTREK</span><span>© Copyright 2019 Lumotrek GmbH. All rights reserved</span><span class="f-dot"></span></div>
</section>

<!-- 30 images + text 2 -->
<section class="slide">
  <div class="s-title">Images + Text</div>
  <div class="photo night" style="left:14px;top:32px;width:200px;height:80px" role="img" aria-label="Glowing network of data lines"></div>
  <div class="abs" style="left:222px;top:36px;width:156px;font-size:7px;color:var(--navy);line-height:1.4">Short statement about our data work and the value it brings to rail operators.</div>
  <div class="abs" style="left:14px;top:118px;width:200px;height:64px;background:var(--ice);padding:8px"><div class="txt">Short text about this topic. It explains one idea in a few plain words and closes with a clear outcome for the reader.</div></div>
  <div class="photo" style="left:222px;right:14px;top:118px;height:64px" role="img" aria-label="Hand touching a digital interface"></div>
  <div class="footer"><span class="f-brand">LUMOTREK</span><span>© Copyright 2019 Lumotrek GmbH. All rights reserved</span><span class="f-dot"></span></div>
</section>

<!-- 31 map -->
<section class="slide">
  <div class="s-title">Editable Germany Map</div>
  <div class="abs" style="left:24px;top:34px;width:140px;height:150px;border-radius:30px 50px 40px 60px;background:linear-gradient(160deg,#c5cad6 0%,#8e97b3 45%,#2a3773 100%)" role="img" aria-label="Map of Germany with highlighted federal states"></div>
  <div class="abs" style="left:190px;top:66px;width:190px">
    <div style="font-size:9px;color:var(--navy);line-height:1.3;margin-bottom:6px">Your beautiful heading goes here, replace this text with your own</div>
    <div class="txt">Short text about the regions where our teams work and the projects we run there.</div>
  </div>
  <div class="footer"><span class="f-brand">LUMOTREK</span><span>© Copyright 2019 Lumotrek GmbH. All rights reserved</span><span class="f-dot"></span></div>
</section>

<!-- 32 heading over photo -->
<section class="slide">
  <div class="photo land" style="inset:0" role="img" aria-label="High-speed train on a line through green hills"></div>
  <div class="abs" style="left:0;top:0;width:190px;bottom:0;background:rgba(20,27,69,.85);padding:46px 14px 0;color:#fff">
    <div style="font-size:12px;font-weight:900">HEADING HERE</div>
    <div class="txt w" style="margin-top:6px;font-size:5.5px">Short text about this route and the services we run on it. It explains the goal and the result in a few plain words for every reader.</div>
  </div>
</section>

<!-- 33 editable icons -->
<section class="slide">
  <div class="s-title">Editable Icons</div>
  <div class="icon-grid" aria-label="Icon set">
    <svg class="ico"><use href="#i-user"/></svg><svg class="ico"><use href="#i-gear"/></svg><svg class="ico"><use href="#i-chart"/></svg><svg class="ico"><use href="#i-globe"/></svg><svg class="ico"><use href="#i-doc"/></svg><svg class="ico"><use href="#i-mail"/></svg><svg class="ico"><use href="#i-phone"/></svg><svg class="ico"><use href="#i-pin"/></svg><svg class="ico"><use href="#i-train"/></svg><svg class="ico"><use href="#i-check"/></svg><svg class="ico"><use href="#i-user"/></svg><svg class="ico"><use href="#i-gear"/></svg><svg class="ico"><use href="#i-chart"/></svg><svg class="ico"><use href="#i-globe"/></svg>
    <svg class="ico"><use href="#i-doc"/></svg><svg class="ico"><use href="#i-train"/></svg><svg class="ico"><use href="#i-pin"/></svg><svg class="ico"><use href="#i-mail"/></svg><svg class="ico"><use href="#i-user"/></svg><svg class="ico"><use href="#i-check"/></svg><svg class="ico"><use href="#i-gear"/></svg><svg class="ico"><use href="#i-phone"/></svg><svg class="ico"><use href="#i-globe"/></svg><svg class="ico"><use href="#i-chart"/></svg><svg class="ico"><use href="#i-train"/></svg><svg class="ico"><use href="#i-doc"/></svg><svg class="ico"><use href="#i-pin"/></svg><svg class="ico"><use href="#i-mail"/></svg>
    <svg class="ico"><use href="#i-chart"/></svg><svg class="ico"><use href="#i-user"/></svg><svg class="ico"><use href="#i-globe"/></svg><svg class="ico"><use href="#i-gear"/></svg><svg class="ico"><use href="#i-phone"/></svg><svg class="ico"><use href="#i-doc"/></svg><svg class="ico"><use href="#i-train"/></svg><svg class="ico"><use href="#i-check"/></svg><svg class="ico"><use href="#i-mail"/></svg><svg class="ico"><use href="#i-pin"/></svg><svg class="ico"><use href="#i-chart"/></svg><svg class="ico"><use href="#i-user"/></svg><svg class="ico"><use href="#i-gear"/></svg><svg class="ico"><use href="#i-globe"/></svg>
    <svg class="ico"><use href="#i-pin"/></svg><svg class="ico"><use href="#i-mail"/></svg><svg class="ico"><use href="#i-check"/></svg><svg class="ico"><use href="#i-train"/></svg><svg class="ico"><use href="#i-doc"/></svg><svg class="ico"><use href="#i-phone"/></svg><svg class="ico"><use href="#i-gear"/></svg><svg class="ico"><use href="#i-user"/></svg><svg class="ico"><use href="#i-chart"/></svg><svg class="ico"><use href="#i-globe"/></svg><svg class="ico"><use href="#i-pin"/></svg><svg class="ico"><use href="#i-train"/></svg><svg class="ico"><use href="#i-doc"/></svg><svg class="ico"><use href="#i-check"/></svg>
    <svg class="ico"><use href="#i-globe"/></svg><svg class="ico"><use href="#i-chart"/></svg><svg class="ico"><use href="#i-mail"/></svg><svg class="ico"><use href="#i-user"/></svg><svg class="ico"><use href="#i-pin"/></svg><svg class="ico"><use href="#i-gear"/></svg><svg class="ico"><use href="#i-check"/></svg><svg class="ico"><use href="#i-train"/></svg><svg class="ico"><use href="#i-phone"/></svg><svg class="ico"><use href="#i-doc"/></svg><svg class="ico"><use href="#i-globe"/></svg><svg class="ico"><use href="#i-mail"/></svg><svg class="ico"><use href="#i-user"/></svg><svg class="ico"><use href="#i-chart"/></svg>
  </div>
  <div class="footer"><span class="f-brand">LUMOTREK</span><span>© Copyright 2019 Lumotrek GmbH. All rights reserved</span><span class="f-dot"></span></div>
</section>

<!-- 34 data chart -->
<section class="slide">
  <div class="s-title">Data Chart</div>
  <div class="photo night" style="left:0;right:0;top:30px;height:110px" role="img" aria-label="Blue-tinted rail infrastructure background"></div>
  <div class="abs" style="left:14px;right:14px;top:46px;display:grid;grid-template-columns:repeat(4,1fr);text-align:center">
    <div><svg width="70" height="70" viewBox="0 0 40 40" class="ring"><circle cx="20" cy="20" r="16" fill="none" stroke="rgba(255,255,255,.3)" stroke-width="3"/><circle cx="20" cy="20" r="16" fill="none" stroke="#fff" stroke-width="3" stroke-dasharray="50.2 100.5" transform="rotate(-90 20 20)"/><text x="20" y="23" text-anchor="middle">50%</text></svg></div>
    <div><svg width="70" height="70" viewBox="0 0 40 40" class="ring"><circle cx="20" cy="20" r="16" fill="none" stroke="rgba(255,255,255,.3)" stroke-width="3"/><circle cx="20" cy="20" r="16" fill="none" stroke="#fff" stroke-width="3" stroke-dasharray="30.2 100.5" transform="rotate(-90 20 20)"/><text x="20" y="23" text-anchor="middle">30%</text></svg></div>
    <div><svg width="70" height="70" viewBox="0 0 40 40" class="ring"><circle cx="20" cy="20" r="16" fill="none" stroke="rgba(255,255,255,.3)" stroke-width="3"/><circle cx="20" cy="20" r="16" fill="none" stroke="#fff" stroke-width="3" stroke-dasharray="10 100.5" transform="rotate(-90 20 20)"/><text x="20" y="23" text-anchor="middle">10%</text></svg></div>
    <div><svg width="70" height="70" viewBox="0 0 40 40" class="ring"><circle cx="20" cy="20" r="16" fill="none" stroke="rgba(255,255,255,.3)" stroke-width="3"/><circle cx="20" cy="20" r="16" fill="none" stroke="#fff" stroke-width="3" stroke-dasharray="20.1 100.5" transform="rotate(-90 20 20)"/><text x="20" y="23" text-anchor="middle">20%</text></svg></div>
  </div>
  <div class="abs" style="left:14px;right:14px;top:148px;display:grid;grid-template-columns:repeat(4,1fr);gap:8px;text-align:center">
    <div><div class="h">Your Title Here</div><div class="txt">Short note here.</div></div>
    <div><div class="h">Your Title Here</div><div class="txt">Short note here.</div></div>
    <div><div class="h">Your Title Here</div><div class="txt">Short note here.</div></div>
    <div><div class="h">Your Title Here</div><div class="txt">Short note here.</div></div>
  </div>
  <div class="footer"><span class="f-brand">LUMOTREK</span><span>© Copyright 2019 Lumotrek GmbH. All rights reserved</span><span class="f-dot"></span></div>
</section>

<!-- 35 latest work -->
<section class="slide">
  <div class="s-title">Our Latest Work</div>
  <div class="abs" style="left:14px;right:14px;top:40px;display:grid;grid-template-columns:repeat(4,1fr);gap:6px;text-align:center">
    <div><div class="photo" style="position:relative;height:60px" role="img" aria-label="Train on a bridge"></div><div class="h" style="margin-top:5px">Start</div><div class="txt">Short note here.</div></div>
    <div><div class="photo truck" style="position:relative;height:60px" role="img" aria-label="Truck on a depot yard"></div><div class="h" style="margin-top:5px">Creative</div><div class="txt">Short note here.</div></div>
    <div><div class="photo land" style="position:relative;height:60px" role="img" aria-label="Rail line in the countryside"></div><div class="h" style="margin-top:5px">Band</div><div class="txt">Short note here.</div></div>
    <div><div class="photo truck" style="position:relative;height:60px" role="img" aria-label="Freight truck on a road"></div><div class="h" style="margin-top:5px">Grow</div><div class="txt">Short note here.</div></div>
  </div>
  <div class="footer"><span class="f-brand">LUMOTREK</span><span>© Copyright 2019 Lumotrek GmbH. All rights reserved</span><span class="f-dot"></span></div>
</section>

<!-- 36 steps cards -->
<section class="slide">
  <div class="s-title">Our Steps</div>
  <div class="step-card" style="left:26px"><div class="st">STEP 01</div><div class="txt">Short note about this step and its result.</div></div>
  <div class="step-card" style="left:144px"><div class="st">STEP 01</div><div class="txt">Short note about this step and its result.</div></div>
  <div class="step-card" style="left:262px"><div class="st">STEP 01</div><div class="txt">Short note about this step and its result.</div></div>
  <div class="abs circle-ico" style="left:61px;top:30px;width:34px;height:34px;background:#fff;border:1.5px solid var(--navy);color:var(--navy)"><svg class="ico"><use href="#i-user"/></svg></div>
  <div class="abs circle-ico" style="left:179px;top:30px;width:34px;height:34px;background:#fff;border:1.5px solid var(--navy);color:var(--navy)"><svg class="ico"><use href="#i-gear"/></svg></div>
  <div class="abs circle-ico" style="left:297px;top:30px;width:34px;height:34px;background:#fff;border:1.5px solid var(--navy);color:var(--navy)"><svg class="ico"><use href="#i-chart"/></svg></div>
  <div class="footer"><span class="f-brand">LUMOTREK</span><span>© Copyright 2019 Lumotrek GmbH. All rights reserved</span><span class="f-dot"></span></div>
</section>

<!-- 37 chevron -->
<section class="slide">
  <div class="s-title">Basic Chevron Process</div>
  <svg class="abs" style="left:14px;top:98px" width="364" height="24" viewBox="0 0 364 24">
    <polygon points="0,0 66,0 76,12 66,24 0,24" fill="#141b45"/>
    <polygon points="72,0 138,0 148,12 138,24 72,24 82,12" fill="#1f2a63"/>
    <polygon points="144,0 210,0 220,12 210,24 144,24 154,12" fill="#2a3773"/>
    <polygon points="216,0 282,0 292,12 282,24 216,24 226,12" fill="#34428a"/>
    <polygon points="288,0 354,0 364,12 354,24 288,24 298,12" fill="#5a68a8"/>
    <g fill="#fff"><circle cx="38" cy="12" r="4"/><circle cx="112" cy="12" r="4"/><circle cx="184" cy="12" r="4"/><circle cx="256" cy="12" r="4"/><circle cx="328" cy="12" r="4"/></g>
  </svg>
  <div class="abs" style="left:30px;top:126px;width:70px;text-align:center"><div class="h">Planning</div><div class="txt">Short note here.</div></div>
  <div class="abs" style="left:96px;top:44px;width:74px;text-align:center"><div class="h">Idea</div><div class="txt">Short note about this stage.</div></div>
  <div class="abs" style="left:166px;top:126px;width:70px;text-align:center"><div class="h">Launch</div><div class="txt">Short note here.</div></div>
  <div class="abs" style="left:236px;top:44px;width:74px;text-align:center"><div class="h">Relationship</div><div class="txt">Short note about this stage.</div></div>
  <div class="abs" style="left:306px;top:126px;width:70px;text-align:center"><div class="h">Services</div><div class="txt">Short note here.</div></div>
  <div class="footer"><span class="f-brand">LUMOTREK</span><span>© Copyright 2019 Lumotrek GmbH. All rights reserved</span><span class="f-dot"></span></div>
</section>

<!-- 38 steps circles -->
<section class="slide">
  <div class="s-title">Our Steps</div>
  <div class="abs" style="left:30px;right:30px;top:82px;height:1.5px;background:var(--navy)"></div>
  <div class="abs" style="left:14px;right:14px;top:44px;display:grid;grid-template-columns:repeat(5,1fr);text-align:center">
    <div><div class="circle-ico" style="width:54px;height:54px;margin:12px auto 0;background:#fff;border:1.5px solid var(--navy);font-size:14px;font-weight:900;color:var(--navy)">01</div><div class="h" style="margin-top:8px">Heading Here</div><div class="txt">Short note here.</div></div>
    <div><div class="circle-ico" style="width:54px;height:54px;margin:12px auto 0;background:#fff;border:1.5px solid var(--navy);font-size:14px;font-weight:900;color:var(--navy)">02</div><div class="h" style="margin-top:8px">Heading Here</div><div class="txt">Short note here.</div></div>
    <div><div class="circle-ico" style="width:54px;height:54px;margin:12px auto 0;background:#fff;border:1.5px solid var(--navy);font-size:14px;font-weight:900;color:var(--navy)">03</div><div class="h" style="margin-top:8px">Heading Here</div><div class="txt">Short note here.</div></div>
    <div><div class="circle-ico" style="width:54px;height:54px;margin:12px auto 0;background:#fff;border:1.5px solid var(--navy);font-size:14px;font-weight:900;color:var(--navy)">04</div><div class="h" style="margin-top:8px">Heading Here</div><div class="txt">Short note here.</div></div>
    <div><div class="circle-ico" style="width:54px;height:54px;margin:12px auto 0;background:#fff;border:1.5px solid var(--navy);font-size:14px;font-weight:900;color:var(--navy)">05</div><div class="h" style="margin-top:8px">Heading Here</div><div class="txt">Short note here.</div></div>
  </div>
  <div class="footer"><span class="f-brand">LUMOTREK</span><span>© Copyright 2019 Lumotrek GmbH. All rights reserved</span><span class="f-dot"></span></div>
</section>

<!-- 39 contact -->
<section class="slide" style="background:var(--navy)">
  <div class="abs" style="right:-30px;top:-20px;width:240px;height:240px;border-radius:50%;background:var(--photo-night)" role="img" aria-label="Tunnel boring site inside a rail tunnel"></div>
  <div class="abs" style="left:16px;top:26px"><div class="brand" style="font-size:13px"><span class="dot"></span>LUMOTREK</div></div>
  <div class="abs" style="left:16px;top:112px;color:#fff;width:170px">
    <div style="font-size:11px;font-weight:900;margin-bottom:6px">CONTACT :</div>
    <div style="display:flex;gap:5px;align-items:center;margin-bottom:4px"><svg class="ico" style="width:8px;height:8px"><use href="#i-mail"/></svg><span class="txt w">kontakt@lumotrek.example</span></div>
    <div style="display:flex;gap:5px;align-items:center;margin-bottom:4px"><svg class="ico" style="width:8px;height:8px"><use href="#i-phone"/></svg><span class="txt w">+49 30 5550 1842</span></div>
    <div style="display:flex;gap:5px;align-items:center;margin-bottom:8px"><svg class="ico" style="width:8px;height:8px"><use href="#i-globe"/></svg><span class="txt w">www.lumotrek.example</span></div>
    <div style="display:flex;gap:5px;align-items:center"><span style="font-size:5.5px;font-weight:700">FOLLOW US :</span><span style="width:8px;height:8px;border-radius:50%;background:#fff"></span><span style="width:8px;height:8px;border-radius:50%;background:#fff"></span><span style="width:8px;height:8px;border-radius:50%;background:#fff"></span><span style="width:8px;height:8px;border-radius:50%;background:#fff"></span></div>
  </div>
</section>

</main>
</body>
</html>
```